Commercial Office Fitout company needs a simple website

We need a website for our company Harbourline Fitouts (QLD) Pty Ltd. We are in the construction industry and we specialise in commercial office fitouts (partitions/glass/doors). Our company colours are black and silver. Please use our logo attached.
We only need an "about us" section, a "portfolio" section where we display some pictures of our work, and a "contact us" section. We would like our website to be simple, effective, professional and modern.

Industry/Entity Type

Construction

Number of Pages Required

1 page

```html
<!DOCTYPE html>
<html lang="en">
<head>
<meta charset="utf-8">
<title>Harbourline Fitouts (QLD) Pty Ltd</title>
<link href="https://fonts.googleapis.com/css2?family=Montserrat:wght@400;500;600&family=Open+Sans:wght@400;600&display=swap" rel="stylesheet">
<style>
:root{
  --ink:#1c1c1c;
  --black:#0b0b0b;
  --header:#12121c;
  --white:#ffffff;
  --silver:#9a9a9a;
  --body-text:#5a5a5a;
  --line:#b8b8b8;
  --footer:#0d0d0d;
  --footer-bar:#161616;
  --footer-text:#cfcfcf;
}
*{margin:0;padding:0;box-sizing:border-box}
html,body{width:1200px;height:2707px;overflow:hidden}
body{position:relative;background:var(--white);font-family:'Open Sans',Arial,sans-serif;color:var(--body-text)}
.abs{position:absolute}
.heading{font-family:'Montserrat',Arial,sans-serif;font-weight:500;color:var(--ink);text-align:center;font-size:31px;letter-spacing:.5px}
.intro{font-size:12.5px;line-height:30px;text-align:center}

/* header */
.site-header{left:0;top:0;width:1200px;height:103px;background:var(--header)}
.brand{left:0;top:0;width:280px;height:103px;background:var(--white);display:flex;align-items:center;justify-content:center;gap:10px}
.brand-mark{width:14px;height:14px;background:var(--ink)}
.brand-name{font-family:'Montserrat',Arial,sans-serif;font-weight:600;font-size:14px;color:var(--ink);line-height:1.2;text-align:center}
.nav a{position:absolute;top:36px;height:31px;line-height:31px;font-family:'Montserrat',Arial,sans-serif;font-size:12px;color:var(--white);text-decoration:none;text-align:center}
.nav .active{border:1px solid var(--white);border-radius:4px;width:74px}

/* hero */
.hero{left:0;top:103px;width:1200px;height:464px;background:linear-gradient(180deg,#2b3050 0%,#3a3a5c 40%,#2a2c3e 75%,#1c2232 100%)}
.hero-title{left:0;top:228px;width:1200px;text-align:center;font-family:'Montserrat',Arial,sans-serif;font-size:40px;color:var(--white);letter-spacing:1px}
.hero-text{left:290px;top:280px;width:620px;text-align:center;color:var(--white);font-size:12.5px;line-height:28px}
.hero-arrow{top:310px}
.scroll{left:570px;top:398px;width:60px;text-align:center;color:var(--white);font-size:10px}

/* about */
.service{width:300px;text-align:center}
.service h3{font-family:'Montserrat',Arial,sans-serif;font-weight:500;font-size:20px;color:var(--ink);margin-top:12px;letter-spacing:.5px}
.service p{font-size:11.5px;line-height:31px;margin-top:8px}

/* portfolio */
.portfolio{left:0;top:1173px;width:1200px;height:731px;background:linear-gradient(160deg,#3a4a52 0%,#24323a 45%,#141c22 100%)}
.portfolio .heading,.portfolio .intro{color:var(--white)}
.tile{width:298px;height:175px;border:4px solid #9da3a8}
.tile-overlay{background:rgba(70,72,74,.92);color:var(--white);text-align:center}
.tile-overlay h4{font-family:'Montserrat',Arial,sans-serif;font-weight:600;font-size:15px;margin-top:30px}
.tile-overlay p{font-size:11.5px;line-height:24px;margin-top:8px;padding:0 30px}

/* contact */
.field{border:1px solid var(--line);font-size:11px;color:#777;padding:0 16px;display:flex;align-items:center}
.field-message{align-items:flex-start;padding-top:14px}
.submit{left:529px;top:2300px;width:141px;height:51px;background:var(--ink);color:var(--white);border-radius:4px;font-family:'Montserrat',Arial,sans-serif;font-size:16px;display:flex;align-items:center;justify-content:center;letter-spacing:.5px}

/* footer */
.site-footer{left:0;top:2401px;width:1200px;height:222px;background:var(--footer);color:var(--footer-text)}
.footer-brand{left:112px;top:42px;width:170px;text-align:center}
.footer-brand .brand-mark{width:14px;height:14px;background:var(--silver);margin:0 auto 8px}
.footer-brand .brand-name{color:var(--silver);font-size:14px}
.footer-about{left:112px;top:124px;width:290px;font-size:11px;line-height:26px;color:var(--footer-text)}
.footer-col h5{font-family:'Montserrat',Arial,sans-serif;font-weight:500;font-size:15px;color:var(--white);margin-bottom:14px}
.footer-col li{list-style:none;font-size:11px;line-height:39px}
.footer-col li::before{content:"›";margin-right:6px}
.footer-contact{left:872px;top:40px;width:260px;font-size:11px;line-height:22px}
.social{display:flex;gap:8px}
.social span{width:24px;height:24px;border-radius:50%;background:#6b6b6b}
.footer-bar{left:0;top:2623px;width:1200px;height:84px;background:var(--footer-bar);color:#9a9a9a;font-size:11px;text-align:center;line-height:84px}
.footer-bar .sitemap{color:#6f6f6f}
</style>
</head>
<body>

<header class="site-header abs">
  <div class="brand abs">
    <span class="brand-mark"></span>
    <span class="brand-name">HARBOURLINE FITOUTS<br>(QLD) PTY LTD</span>
  </div>
  <nav class="nav">
    <a class="active" style="left:617px">HOME</a>
    <a style="left:746px">ABOUT US</a>
    <a style="left:881px">PORTFOLIO</a>
    <a style="left:1018px">CONTACT US</a>
  </nav>
</header>

<section class="hero abs" role="img" aria-label="Night photograph of a harbour city skyline with an opera house and lit office towers">
</section>
<svg class="abs hero-arrow" style="left:30px" width="26" height="48" viewBox="0 0 26 48"><polyline points="22,2 4,24 22,46" fill="none" stroke="#fff" stroke-width="1.5" opacity=".7"/></svg>
<svg class="abs hero-arrow" style="left:1144px" width="26" height="48" viewBox="0 0 26 48"><polyline points="4,2 22,24 4,46" fill="none" stroke="#fff" stroke-width="1.5" opacity=".7"/></svg>
<h1 class="hero-title abs">COMMERCIAL OFFICE FITOUTS</h1>
<p class="hero-text abs">Lorem ipsum dolor sit amet, consectetur adipiscing elit. Vestibulum laoreet accumsan varius. Phasellus non arcu et magna lacinia cursus. Integer vitae lectus sit amet nulla luctus cursus.</p>
<div class="scroll abs">SCROLL
  <svg width="12" height="20" viewBox="0 0 12 20" style="display:block;margin:4px auto 0"><rect x="1" y="1" width="10" height="18" rx="5" fill="none" stroke="#fff"/><line x1="6" y1="5" x2="6" y2="9" stroke="#fff"/></svg>
</div>

<section class="about">
  <h2 class="heading abs" style="left:0;top:620px;width:1200px">ABOUT US</h2>
  <p class="intro abs" style="left:110px;top:673px;width:980px">Nullam quis tempor nisl. Aenean auctor diam sed ex eleifend, maximus semper felis condimentum. Curabitur imperdiet, tellus sit amet ullamcorper congue, lorem orci venenatis ligula, in congue nisi metus eget nulla. Nam lacus lacus, tempus id molestie sit amet, rhoncus non mi. Aenean et tincidunt ligula.</p>

  <div class="service abs" style="left:115px;top:770px">
    <svg width="150" height="160" viewBox="0 0 150 160">
      <polygon points="75,2 145,42 145,118 75,158 5,118 5,42" fill="none" stroke="#1c1c1c" stroke-width="2"/>
      <polygon points="75,9 139,46 139,114 75,151 11,114 11,46" fill="#1c1c1c"/>
      <g fill="#fff"><rect x="52" y="58" width="46" height="46"/></g>
      <g fill="#1c1c1c"><rect x="57" y="64" width="6" height="6"/><rect x="67" y="64" width="6" height="6"/><rect x="77" y="64" width="6" height="6"/><rect x="87" y="64" width="6" height="6"/><rect x="57" y="76" width="6" height="6"/><rect x="67" y="76" width="6" height="6"/><rect x="77" y="76" width="6" height="6"/><rect x="87" y="76" width="6" height="6"/><rect x="70" y="90" width="10" height="14"/></g>
    </svg>
    <h3>PARTITIONS</h3>
    <p>Curabitur imperdiet, tellus sit amet ullamcorper congue, lorem orci venenatis ligula, in congue nisi me tus eget nulla. Nam lacus lacus.</p>
  </div>

  <div class="service abs" style="left:450px;top:770px">
    <svg width="150" height="160" viewBox="0 0 150 160">
      <polygon points="75,2 145,42 145,118 75,158 5,118 5,42" fill="none" stroke="#1c1c1c" stroke-width="2"/>
      <polygon points="75,9 139,46 139,114 75,151 11,114 11,46" fill="#1c1c1c"/>
      <rect x="50" y="52" width="50" height="56" fill="none" stroke="#fff" stroke-width="3"/>
      <g fill="none" stroke="#fff" stroke-width="2"><rect x="56" y="58" width="16" height="20"/><rect x="78" y="58" width="16" height="20"/><rect x="56" y="83" width="16" height="20"/><rect x="78" y="83" width="16" height="20"/></g>
    </svg>
    <h3>GLASS</h3>
    <p>Praesent id urna est. Vivamus blandit, justo ut volu tpat fermentum, purus elit venenatis ipsum, sed venenatis enim quam non ligula.</p>
  </div>

  <div class="service abs" style="left:783px;top:770px">
    <svg width="150" height="160" viewBox="0 0 150 160">
      <polygon points="75,2 145,42 145,118 75,158 5,118 5,42" fill="none" stroke="#1c1c1c" stroke-width="2"/>
      <polygon points="75,9 139,46 139,114 75,151 11,114 11,46" fill="#1c1c1c"/>
      <rect x="56" y="52" width="38" height="56" fill="none" stroke="#fff" stroke-width="3"/>
      <polygon points="60,56 82,62 82,108 60,104" fill="#fff"/>
      <circle cx="77" cy="84" r="2" fill="#1c1c1c"/>
    </svg>
    <h3>DOORS</h3>
    <p>Aliquam eros metus, tincidunt eget cursus in, egesta at est. Nulla posuere a ex sit amet condimentum. Sed molestie quam at magna accum.</p>
  </div>
</section>

<section class="portfolio abs" role="img" aria-label="Dark photograph of a glass office tower facade seen from below">
  <h2 class="heading abs" style="left:0;top:77px;width:1200px">OUR PORTFOLIO</h2>
  <p class="intro abs" style="left:190px;top:140px;width:820px;line-height:22px">Vivamus tincidunt elementum sapien quis sodales. Proin eu est quis magna sagittis efficitur. Vestibulum non sapien eleifend, auctor sapien eu, faucibus urna. Fusce at sem tellus. Duis gravida placerat mauris non vestibulum. Proin maximus suscipit sollicitudin.</p>

  <div class="tile abs" style="left:114px;top:240px;background:linear-gradient(135deg,#e6e2dc 0%,#c9b8a4 55%,#7a4e32 100%)" role="img" aria-label="Empty office interior with timber floor and glass partitions"></div>
  <div class="tile abs" style="left:451px;top:240px;background:linear-gradient(135deg,#3c7fb8 0%,#a8d0ea 50%,#f1e7c8 70%,#3d6b8e 100%)" role="img" aria-label="Glass-walled office with sunlight over a city view"></div>
  <div class="tile abs" style="left:789px;top:240px;background:linear-gradient(135deg,#7fa9c4 0%,#d4e2ea 55%,#f3dcae 100%)" role="img" aria-label="Open office floor with glass balustrades"></div>
  <div class="tile abs" style="left:114px;top:455px;background:linear-gradient(180deg,#2d6fd6 0%,#5b8fd8 45%,#c47a3a 80%,#3a3a46 100%)" role="img" aria-label="Modern office building at dusk"></div>
  <div class="tile tile-overlay abs" style="left:451px;top:455px">
    <h4>LOREM IPSUM DOLOR SIT</h4>
    <p>Curabitur fringilla ultrices arcu, et pellente sque erat gravida sed. Nulla facilisi.</p>
    <svg width="26" height="26" viewBox="0 0 26 26" style="margin-top:4px"><circle cx="13" cy="13" r="13" fill="#fff"/><path d="M13 7v12M7 13h12" stroke="#46484a" stroke-width="3"/></svg>
  </div>
  <div class="tile abs" style="left:789px;top:455px;background:linear-gradient(135deg,#f4f4f4 0%,#e0e2e6 55%,#9aa3b4 100%)" role="img" aria-label="Bright white office with workstations"></div>
</section>

<section class="contact">
  <h2 class="heading abs" style="left:0;top:1961px;width:1200px">CONTACT US</h2>
  <p class="intro abs" style="left:110px;top:2016px;width:980px">Nunc ante ipsum, venenatis vel facilisis eu, rutrum et nisi. Mauris ut nisl eu diam iaculis viverra. Fusce nec commodo erat, sollicitudin auctor nunc. Praesent id urna est. Vivamus blandit, justo ut volutpat fermentum, purus elit venenatis ipsum, sed venenatis enim quam non ligula.</p>
  <div class="field abs" style="left:112px;top:2105px;width:468px;height:45px">Name</div>
  <div class="field abs" style="left:112px;top:2164px;width:468px;height:45px">Email Address</div>
  <div class="field abs" style="left:112px;top:2224px;width:468px;height:45px">Phone</div>
  <div class="field field-message abs" style="left:619px;top:2105px;width:469px;height:164px">Message</div>
  <div class="submit abs">SUBMIT</div>
</section>

<footer class="site-footer abs">
  <div class="footer-brand abs">
    <span class="brand-mark" style="display:block"></span>
    <span class="brand-name">HARBOURLINE FITOUTS<br>(QLD) PTY LTD</span>
  </div>
  <p class="footer-about abs">Lorem ipsum dolor sit amet, consectetuer adipiscing elit, sed diam nonummy nibh euismod tincidunt ut laoreet dol ore magna aliquam erat volutpat.</p>
  <div class="footer-col abs" style="left:475px;top:40px">
    <h5>ABOUT US</h5>
    <ul><li>About us</li><li>Portfolio</li><li>Contact Us</li></ul>
  </div>
  <div class="footer-col abs" style="left:662px;top:40px">
    <h5>QUICK LINKS</h5>
    <ul><li>Get started</li><li>Careers</li><li>Privacy &amp; Terms</li></ul>
  </div>
  <div class="footer-contact abs">
    <div style="display:flex;gap:14px">
      <svg width="18" height="24" viewBox="0 0 18 24"><path d="M9 0a9 9 0 0 0-9 9c0 7 9 15 9 15s9-8 9-15a9 9 0 0 0-9-9z" fill="#fff"/><circle cx="9" cy="9" r="3.5" fill="#0d0d0d"/></svg>
      <div>11 Lorem Ipsm, Lorem<br>Lorem Ipsm 07662</div>
    </div>
    <div style="display:flex;gap:12px;margin-top:10px">
      <svg width="24" height="24" viewBox="0 0 24 24"><rect width="24" height="24" rx="4" fill="#fff"/><path d="M7 5l3 3-2 2c1 2 3 4 5 5l2-2 3 3-2 3c-5 0-11-6-11-11z" fill="#0d0d0d"/></svg>
      <div>Telephone: (07) 3100 4820<br>Mail : hello@harbourlinefitouts.example</div>
    </div>
    <div class="social" style="margin:16px 0 0 2px"><span></span><span></span><span></span><span></span></div>
  </div>
</footer>
<div class="footer-bar abs">Harbourline Fitouts (QLD) Pty Ltd © 2016 • <span class="sitemap">Sitemap</span></div>

</body>
</html>
```